Non-profit wants to save the world needs Wordpress presence

My name is Marco Estelani. I'm a photographer who started a charity (Rancho las Brisas) to help the rural schools and health clinics in Central America. We distribute schools supplies and help health clinics with much needed medical supplies and equipment. I need a way to accept donations. I need to have several different writers post to the blog (in Spanish and English). I have a domain name registered (www.rancholasbrisas.org) and started a simple wordpress site as well at http://www.rancholasbrisas.wordpress.com

Industry/Entity Type

Charity

```html
<!DOCTYPE html>
<html lang="en">
<head>
<meta charset="utf-8">
<title>Rancho las Brisas</title>
<link href="https://fonts.googleapis.com/css2?family=Source+Sans+3:ital,wght@0,400;0,600;0,700;1,400;1,600&display=swap" rel="stylesheet">
<style>
:root{
  --dark:#231f20;
  --rust:#a4520a;
  --green:#77b243;
  --green-deep:#5a9a2a;
  --green-text:#4f8a2a;
  --text:#3c3c3c;
  --muted:#6a6a6a;
  --box:#f1f1f1;
  --box-line:#d7d7d7;
  --white:#fff;
}
*{margin:0;padding:0;box-sizing:border-box}
html,body{width:791px;height:1200px;overflow:hidden}
body{background:var(--dark);font-family:"Source Sans 3",sans-serif;color:var(--text);position:relative}
.abs{position:absolute}
.top-band{left:0;top:0;width:791px;height:8px;background:var(--rust)}
.bottom-band{left:0;top:1184px;width:791px;height:16px;background:var(--rust);color:#f3d6b8;font-size:8px;text-align:center;line-height:16px}
.page{left:66px;top:8px;width:660px;height:1024px;background:var(--white)}

.brand{left:75px;top:20px;display:flex;align-items:center;gap:6px}
.brand-mark{width:34px;height:34px;border-radius:50%;background:var(--green)}
.brand-name{font-size:17px;font-weight:700;color:var(--green-text);line-height:1;width:70px}
.tagline{left:204px;top:49px;font-size:22px;font-weight:600;color:#4b4b4b;letter-spacing:.2px}
.donate{left:612px;top:31px;width:102px;height:69px;background:linear-gradient(#8cc152,#6aa536);border:1px solid #5f9a33;box-shadow:0 5px 4px -2px #9a9a9a;color:var(--white);text-align:center}
.donate-name{font-size:15px;font-weight:700;margin-top:16px}
.donate-call{font-size:7.5px;margin-top:6px}

.nav{left:78px;top:123px;width:638px;height:33px;background:var(--green);border-radius:3px;display:flex;justify-content:center;align-items:center}
.nav a{color:var(--white);font-size:11px;font-weight:700;text-decoration:none;padding:2px 9px;border-left:1px solid #a7d37f;line-height:13px}
.nav a:first-child{border-left:none}
.nav a.current{background:#9ccc6c;border-radius:3px;margin-right:4px;padding:3px 5px}

.hero{left:78px;top:176px;width:427px;height:209px;background:linear-gradient(160deg,#3f5a2a,#6e7d55 45%,#8a8268)}

.panel{background:linear-gradient(#f7f7f7,#ececec);border:2px solid var(--box-line);border-radius:3px}
.connect{left:519px;top:176px;width:197px;height:81px}
.panel-title{font-size:14px;font-weight:700;color:var(--green-text);letter-spacing:.3px}
.connect .panel-title{text-align:center;margin-top:5px}
.social{display:flex;gap:8px;justify-content:center;margin-top:7px}
.social span{width:33px;height:33px;border-radius:50%;border:2px solid #c9c9c9;background:var(--white)}
.newsletter{left:519px;top:262px;width:197px;height:123px;background:linear-gradient(#9bd063,#5b9c2c);border-radius:3px;padding:9px 12px;color:#fff}
.newsletter h3{font-size:15px;font-weight:600;color:#2f4a1d}
.newsletter p{font-size:7.5px;line-height:10px;color:#2f4a1d;margin-top:10px}
.email{margin-top:12px;display:flex;height:25px;border:2px solid #e6e6e6;border-radius:4px;background:#fff}
.email span{flex:1;background:#ececec;font-size:7px;font-style:italic;color:#888;padding:8px 12px 0}
.email svg{width:30px;height:21px}

.welcome{left:80px;top:402px;width:425px}
.welcome h1{font-size:21px;font-weight:400;color:#3a3a3a}
.welcome h1 em{color:var(--green);font-weight:600}
.welcome p{font-size:12.5px;line-height:18.4px;margin-top:6px;color:#444}

.post{left:81px;width:421px;height:160px}
.post-img{position:absolute;left:0;top:0;width:155px;height:106px;border:2px solid #c8c8c8}
.post-body{position:absolute;left:175px;top:0;width:250px}
.post h2{font-size:15px;font-weight:400;line-height:19px;color:#333}
.meta{display:flex;align-items:center;font-size:8.5px;color:var(--green);margin-top:7px}
.meta .dot{margin:0 7px}
.meta .shares{margin-left:auto;display:flex;gap:5px;margin-right:14px}
.meta .shares i{width:13px;height:13px;border-radius:50%;background:#8a8a8a}
.post p{font-size:7px;line-height:11.2px;color:#666;margin-top:9px}
.rule{left:83px;width:417px;height:1px;background:#cfcfcf}

.older{left:519px;top:412px;width:197px;height:178px;padding:14px 14px}
.arrows{position:absolute;right:10px;top:17px;display:flex;gap:1px}
.arrows span{width:10px;height:10px;background:#5f8d3a}
.older-item{display:flex;gap:7px;margin-top:18px}
.older-item + .older-item{border-top:1px solid #d5d5d5;padding-top:12px;margin-top:10px}
.older-thumb{width:38px;height:32px;flex:none;background:linear-gradient(#6f8fb0,#8a7060)}
.older-item b{display:block;font-size:6px;line-height:7px;font-weight:600;color:#333}
.older-item small{display:block;font-size:4.5px;line-height:6.5px;color:#888;margin-top:2px}
.older-item small em{color:var(--green);font-style:normal}

.video{left:522px;top:635px;width:190px;height:114px;background:linear-gradient(150deg,#2f3f25,#5c6048 60%,#3a3a30)}
.video svg{position:absolute;left:0;top:0}

.news{left:519px;top:795px;width:197px;height:179px;padding:16px 0 0 20px}
.news ul{list-style:none;margin-top:15px}
.news li{font-size:9px;color:#555;display:flex;align-items:center;gap:8px;height:21.3px}
.news li svg{width:11px;height:8px;flex:none}

.foot-col{top:1048px;color:#fff}
.foot-col h4{font-size:14px;font-weight:600}
.foot-about{left:106px;width:200px}
.foot-about p{font-size:8px;line-height:16px;margin-top:6px}
.foot-links ul{list-style:none;font-size:9px;font-weight:600;line-height:14px;margin-top:4px;padding-left:15px}
.foot-archive ul{padding-left:2px}
.foot-tags p{font-size:9px;font-weight:700;line-height:15px;margin-top:4px;width:100px}
</style>
</head>
<body>
<div class="abs top-band"></div>
<div class="abs page"></div>

<div class="abs brand">
  <span class="brand-mark"></span>
  <span class="brand-name">Rancho las Brisas</span>
</div>
<div class="abs tagline">Cultivando la paz y puro amor</div>
<div class="abs donate">
  <div class="donate-name">GiveRoot</div>
  <div class="donate-call">Click to Donate Now!</div>
</div>

<nav class="abs nav">
  <a class="current">Home</a><a>About Me</a><a>Our Projects</a><a>Blogs</a><a>News</a><a>Support Us</a><a>Contact Us</a>
</nav>

<div class="abs hero" role="img" aria-label="Photographer kneeling on a rural path taking pictures of children, with villagers walking among trees"></div>

<aside class="abs panel connect">
  <div class="panel-title">KEEP CONNECTED</div>
  <div class="social"><span></span><span></span><span></span><span></span></div>
</aside>

<aside class="abs newsletter">
  <h3>Sign up to our Newsletter</h3>
  <p>Lorem ipsum dolor sit amet, consectetur adipisicing elit, sed do eiusmod tempor.</p>
  <div class="email">
    <span>Enter your Email</span>
    <svg viewBox="0 0 30 21"><path d="M9 10.5h11M15 6l5 4.5-5 4.5" stroke="#4f8a2a" stroke-width="2.2" fill="none"/></svg>
  </div>
</aside>

<section class="abs welcome">
  <h1>Welcome to <em>Rancho las Brisas</em></h1>
  <p>Lorem ipsum dolor sit amet, consectetur adipisicing elit, sed do eiusmod tempor incididunt ut labore et dolore magna aliqua. Ut enim ad minim veniam, quis nostrud exercitation ullamco laboris nisi ut aliquip ex ea commodo consequat. Duis aute irure dolor in reprehenderit in voluptate velit esse cillum.</p>
</section>

<article class="abs post" style="top:542px">
  <div class="post-img" role="img" aria-label="Man standing beside a wooden shed with a green tarp" style="background:linear-gradient(120deg,#8a6e48,#5c7a50 55%,#c8b89a)"></div>
  <div class="post-body">
    <h2>Lorem ipsum dolor sit amet, consect etur adipisicing elit...</h2>
    <div class="meta"><span>September 24</span><span class="dot">•</span><span>14 Comments</span><span class="shares"><i></i><i></i><i></i></span></div>
    <p>Lorem ipsum dolor sit amet, consectetur adipisicing elit, sed do eiusmod tempor incididunt ut labore et dolore magna aliqua. Ut enim ad minim veniam, quis nostrud exercitation ullamco laboris nisi ut aliquip ex ea commodo consequat. Duis aute irure dolor in.</p>
  </div>
</article>
<div class="abs rule" style="top:668px"></div>

<article class="abs post" style="top:707px">
  <div class="post-img" role="img" aria-label="Man greeting a group of village children on a dirt street" style="background:linear-gradient(120deg,#d9d9d9,#9a8a78 50%,#6b7a8a)"></div>
  <div class="post-body">
    <h2>Lorem ipsum dolor sit amet, consect etur adipisicing elit...</h2>
    <div class="meta"><span>September 24</span><span class="dot">•</span><span>14 Comments</span><span class="shares"><i></i><i></i><i></i></span></div>
    <p>Lorem ipsum dolor sit amet, consectetur adipisicing elit, sed do eiusmod tempor incididunt ut labore et dolore magna aliqua. Ut enim ad minim veniam, quis nostrud exercitation ullamco laboris nisi ut aliquip ex ea commodo consequat. Duis aute irure dolor in.</p>
  </div>
</article>
<div class="abs rule" style="top:833px"></div>

<article class="abs post" style="top:877px">
  <div class="post-img" role="img" aria-label="Two smiling girls in front of a brick wall" style="background:linear-gradient(120deg,#b8c0b0,#c9a88a 50%,#9aa6a0)"></div>
  <div class="post-body">
    <h2>Lorem ipsum dolor sit amet, consect etur adipisicing elit...</h2>
    <div class="meta"><span>September 24</span><span class="dot">•</span><span>14 Comments</span><span class="shares"><i></i><i></i><i></i></span></div>
    <p>Lorem ipsum dolor sit amet, consectetur adipisicing elit, sed do eiusmod tempor incididunt ut labore et dolore magna aliqua. Ut enim ad minim veniam, quis nostrud exercitation ullamco laboris nisi ut aliquip ex ea commodo consequat. Duis aute irure dolor in.</p>
  </div>
</article>
<div class="abs rule" style="top:1003px"></div>

<aside class="abs panel older">
  <div class="panel-title">OLDER POSTS</div>
  <div class="arrows"><span></span><span></span></div>
  <div class="older-item">
    <div class="older-thumb" role="img" aria-label="Group of children standing together"></div>
    <div><b>Lorem ipsum dolor sit amet, consectetur adipisicing elit..</b><small>Lorem ipsum dolor sit amet, consectetur adipisicing elit, sed do eiusmod tempor ut labore et dolore magna aliqua <em>[READ MORE]</em></small></div>
  </div>
  <div class="older-item">
    <div class="older-thumb" role="img" aria-label="Group of children standing together"></div>
    <div><b>Lorem ipsum dolor sit amet, consectetur adipisicing elit..</b><small>Lorem ipsum dolor sit amet, consectetur adipisicing elit, sed do eiusmod tempor ut labore et dolore magna aliqua <em>[READ MORE]</em></small></div>
  </div>
</aside>

<div class="abs video" role="img" aria-label="Video still of the photographer at work on a village path">
  <svg width="190" height="114" viewBox="0 0 190 114">
    <circle cx="125" cy="57" r="24" fill="rgba(0,0,0,.25)" stroke="#fff" stroke-width="2.5"/>
    <path d="M119 46l17 11-17 11z" fill="#fff"/>
    <rect x="0" y="106" width="190" height="8" fill="#1b1b1b"/>
    <rect x="0" y="106" width="190" height="2" fill="#555"/>
    <rect x="0" y="106" width="10" height="2" fill="#c00"/>
  </svg>
</div>

<aside class="abs panel news">
  <div class="panel-title">LATEST NEWS &amp; EVENTS</div>
  <ul>
    <li><svg viewBox="0 0 11 8"><path d="M1 1l3 3-3 3M6 1l3 3-3 3" stroke="#4a9aa8" stroke-width="1.6" fill="none"/></svg>Lorem ipsum dolor sit amet,</li>
    <li><svg viewBox="0 0 11 8"><path d="M1 1l3 3-3 3M6 1l3 3-3 3" stroke="#4a9aa8" stroke-width="1.6" fill="none"/></svg>Consectetur adipisicing elit, sed do</li>
    <li><svg viewBox="0 0 11 8"><path d="M1 1l3 3-3 3M6 1l3 3-3 3" stroke="#4a9aa8" stroke-width="1.6" fill="none"/></svg>Eiusmod tempor incididunt ut</li>
    <li><svg viewBox="0 0 11 8"><path d="M1 1l3 3-3 3M6 1l3 3-3 3" stroke="#4a9aa8" stroke-width="1.6" fill="none"/></svg>Labore et dolore magna aliqua. Ut</li>
    <li><svg viewBox="0 0 11 8"><path d="M1 1l3 3-3 3M6 1l3 3-3 3" stroke="#4a9aa8" stroke-width="1.6" fill="none"/></svg>Enim ad minim veniam, quis irure</li>
  </ul>
</aside>

<footer>
  <div class="abs foot-col foot-about">
    <h4>About Me</h4>
    <p>Lorem ipsum dolor sit amet, consectetur adipisicing elit, sed do eiusmod tempor incididunt ut labore et dolore magna aliqua. Ut enim ad minim veniam, quis nostrud exercitation ullamco laboris nisi ut aliquip ex ea commodo consequat.</p>
  </div>
  <div class="abs foot-col foot-links" style="left:349px">
    <h4>Quick Links</h4>
    <ul><li>Home</li><li>About Us</li><li>Our Projects</li><li>Blogs</li><li>News</li><li>Support Us</li><li>Contact Us</li></ul>
  </div>
  <div class="abs foot-col foot-links foot-archive" style="left:483px">
    <h4>Archives</h4>
    <ul><li>January (6)</li><li>February (9)</li><li>March (4)</li><li>April (4)</li><li>June (5)</li><li>July (7)</li><li>August (8)</li></ul>
  </div>
  <div class="abs foot-col foot-tags" style="left:588px">
    <h4 style="padding-left:26px">Tags</h4>
    <p>News, dolor sit amet, consectetur, BLOGS, adipisicing elit, sed do eiusmod, tempor, Donation, ut labore et</p>
  </div>
</footer>

<div class="abs bottom-band">Copyright@rancholasbrisas.2014.All Rights Reserved.</div>
</body>
</html>
```